A-Stand Directional Sign Design

Objective:
We need a professional graphic design for an A-Stand sign that will guide customers arriving in our parking lot to our office. The design should be visually clear, welcoming, and aligned with our brand identity.
REQUIREMENTS:
Two versions of the design:
- One with an arrow pointing left
- One with an arrow pointing right
(This allows us to place the A-Stand anywhere and flip the graphic as needed.)
DIMENSIONS:
- Viewable Area: 30" x 40"
BRAND ALIGNMENT:
- Colors, fonts, and overall style should match our website: www.skornabel.com
- Clean, modern, and professional look consistent with our aviation/tourism brand
CONTENT:
- Clear directional arrow (left or right depending on version)
- Text: “Office Entrance” or similar concise wording (designers may propose alternatives if they improve clarity)
READABILITY:
- Bold, high-contrast design for visibility from a distance
- Simple layout that avoids clutter
DELIVERABLES:
- Final artwork in print-ready format (PDF preferred)
- Two versions: Arrow Left and Arrow Right
DESIGN GOAL:
Ensure customers can easily find our office upon arrival, while reinforcing skorNABEL’s professional and welcoming brand image.
Target Market(s)
Tourism

```html
<!DOCTYPE html>
<html lang="en">
<head>
<meta charset="utf-8">
<title>skorNABEL – Office Entrance A-Stand Signs</title>
<link href="https://fonts.googleapis.com/css2?family=Montserrat:wght@500;600;800&display=swap" rel="stylesheet">
<style>
  :root {
    --board-blue: #85abd5;
    --brand-blue: #2878b6;
    --sky-blue: #87aad4;
    --white: #ffffff;
    --floor-grey: #e6e9ee;
  }
  html, body {
    margin: 0;
    padding: 0;
    width: 1200px;
    height: 3333px;
    overflow: hidden;
  }
  body {
    position: relative;
    background: var(--floor-grey);
    font-family: "Montserrat", sans-serif;
  }
  .presentation-board {
    position: absolute;
    left: 0;
    top: 0;
    width: 1200px;
    height: 2427px;
    background: var(--board-blue);
  }
  .sign {
    position: absolute;
    width: 500px;
    height: 665px;
    box-shadow: 0 10px 40px rgba(30, 70, 130, 0.45);
  }
  .sign--white { background: var(--white); --title: var(--brand-blue); --sub: var(--sky-blue); --arrow: var(--sky-blue); --brand: var(--brand-blue); }
  .sign--brand { background: var(--brand-blue); --title: var(--sky-blue); --sub: var(--white); --arrow: var(--white); --brand: var(--white); }
  .sign--sky   { background: var(--sky-blue); --title: var(--brand-blue); --sub: var(--white); --arrow: var(--white); --brand: var(--brand-blue); }

  .col-left  { left: 67px; }
  .col-right { left: 630px; }
  .row-1 { top: 114px; }
  .row-2 { top: 875px; }
  .row-3 { top: 1636px; }

  .sign__title {
    position: absolute;
    left: 67px;
    top: 52px;
    width: 366px;
    margin: 0;
    font-weight: 500;
    font-size: 92px;
    line-height: 1;
    letter-spacing: -1px;
    text-align: center;
    color: var(--title);
  }
  .sign__subtitle {
    position: absolute;
    left: 67px;
    top: 146px;
    width: 366px;
    margin: 0;
    font-weight: 800;
    font-size: 61px;
    line-height: 1;
    letter-spacing: 2px;
    text-align: center;
    color: var(--sub);
  }
  .sign__arrow {
    position: absolute;
    left: 85px;
    top: 268px;
    width: 346px;
    height: 141px;
    fill: var(--arrow);
  }
  .sign__arrow--right { transform: scaleX(-1); }
  .sign__brand {
    position: absolute;
    left: 150px;
    top: 552px;
    width: 284px;
    display: flex;
    align-items: center;
    justify-content: flex-end;
    gap: 12px;
    font-weight: 600;
    font-size: 36px;
    color: var(--brand);
  }
  .sign__brand-dot {
    width: 18px;
    height: 18px;
    border-radius: 50%;
    background: var(--brand);
  }
  .sign--featured {
    left: 397px;
    top: 2610px;
    transform: scale(0.812);
    transform-origin: top left;
  }
</style>
</head>
<body>
  <svg width="0" height="0" style="position:absolute">
    <defs>
      <polygon id="arrow-shape" points="0,70 173,0 139,58 346,58 346,83 139,83 173,141"/>
    </defs>
  </svg>

  <section class="presentation-board">
    <article class="sign sign--white col-left row-1">
      <h2 class="sign__title">OFFICE</h2>
      <p class="sign__subtitle">ENTRANCE</p>
      <svg class="sign__arrow" viewBox="0 0 346 141"><use href="#arrow-shape"/></svg>
      <div class="sign__brand"><span class="sign__brand-dot"></span>skorNABEL</div>
    </article>
    <article class="sign sign--white col-right row-1">
      <h2 class="sign__title">OFFICE</h2>
      <p class="sign__subtitle">ENTRANCE</p>
      <svg class="sign__arrow sign__arrow--right" viewBox="0 0 346 141"><use href="#arrow-shape"/></svg>
      <div class="sign__brand"><span class="sign__brand-dot"></span>skorNABEL</div>
    </article>

    <article class="sign sign--brand col-left row-2">
      <h2 class="sign__title">OFFICE</h2>
      <p class="sign__subtitle">ENTRANCE</p>
      <svg class="sign__arrow" viewBox="0 0 346 141"><use href="#arrow-shape"/></svg>
      <div class="sign__brand"><span class="sign__brand-dot"></span>skorNABEL</div>
    </article>
    <article class="sign sign--brand col-right row-2">
      <h2 class="sign__title">OFFICE</h2>
      <p class="sign__subtitle">ENTRANCE</p>
      <svg class="sign__arrow sign__arrow--right" viewBox="0 0 346 141"><use href="#arrow-shape"/></svg>
      <div class="sign__brand"><span class="sign__brand-dot"></span>skorNABEL</div>
    </article>

    <article class="sign sign--sky col-left row-3">
      <h2 class="sign__title">OFFICE</h2>
      <p class="sign__subtitle">ENTRANCE</p>
      <svg class="sign__arrow" viewBox="0 0 346 141"><use href="#arrow-shape"/></svg>
      <div class="sign__brand"><span class="sign__brand-dot"></span>skorNABEL</div>
    </article>
    <article class="sign sign--sky col-right row-3">
      <h2 class="sign__title">OFFICE</h2>
      <p class="sign__subtitle">ENTRANCE</p>
      <svg class="sign__arrow sign__arrow--right" viewBox="0 0 346 141"><use href="#arrow-shape"/></svg>
      <div class="sign__brand"><span class="sign__brand-dot"></span>skorNABEL</div>
    </article>
  </section>

  <article class="sign sign--sky sign--featured">
    <h2 class="sign__title">OFFICE</h2>
    <p class="sign__subtitle">ENTRANCE</p>
    <svg class="sign__arrow sign__arrow--right" viewBox="0 0 346 141"><use href="#arrow-shape"/></svg>
    <div class="sign__brand"><span class="sign__brand-dot"></span>skorNABEL</div>
  </article>
</body>
</html>
```